Vantrel Web Services

This is a new It services company operating in Perth western Australia

we need a website that is easy to navigate without a cluttered feel to it it should have the following links and pages

About Us
Services
Clients
Contact Us
MY Vantrel (login for clients)

Hi it is a web based IT services company so we would expect customers to come to the website for 2 different purposes the first is to enquire about our services and then as they become customers come to our website to manage their services so whilst they are seperate we want do not want it to look like 2 different websites

hope this helps

Hi to update this we need a home page and templates for sub pages

this is a design brief only and not the coding of the pages or building of the site

```html
<!DOCTYPE html>
<html lang="en">
<head>
<meta charset="utf-8">
<title>Vantrel Web Services</title>
<link rel="stylesheet" href="https://fonts.googleapis.com/css2?family=Montserrat:wght@400;600;700&family=Open+Sans:wght@400;600;700&display=swap">
<style>
:root{
  --blue:#1a2f9c;
  --topbar:#1577d8;
  --red:#b01a1a;
  --navy:#0e1a33;
  --text:#333;
  --muted:#666;
  --grey:#efeff1;
  --line:#e2e2e2;
  --white:#fff;
}
*{margin:0;padding:0;box-sizing:border-box}
html,body{width:1200px;height:2837px;overflow:hidden}
body{position:relative;background:var(--white);font-family:"Open Sans",Arial,sans-serif;color:var(--text)}
.abs{position:absolute}
.heading{font-family:"Montserrat",Arial,sans-serif;font-weight:700;color:var(--blue);text-align:center;letter-spacing:1px}

/* top bar */
.top-bar{left:0;top:0;width:1200px;height:34px;background:var(--topbar)}
.top-link{top:0;height:34px;line-height:34px;color:#fff;font-size:14px;font-weight:700;text-align:center}
.top-link.account{left:814px;width:142px;background:var(--red)}
.top-link.register{left:956px;width:108px;background:#0e3f8c}

/* header */
.site-header{left:0;top:34px;width:1200px;height:96px;background:#fff}
.brand{left:142px;top:58px;display:flex;align-items:center;gap:12px}
.brand-dot{width:52px;height:52px;border-radius:50%;background:var(--red)}
.brand-name{font-family:"Montserrat",Arial,sans-serif;font-weight:700;font-size:34px;color:var(--red)}
.main-nav{top:74px;left:652px;display:flex;gap:0}
.main-nav span{font-family:"Montserrat",Arial,sans-serif;font-weight:600;font-size:15px;color:#222;margin-right:30px}

/* hero */
.hero{left:0;top:130px;width:1200px;height:528px;background:linear-gradient(90deg,#e9edf3 0%,#f3f6fa 40%,#d9e2ec 70%,#c3d1df 100%)}
.hero-photo{left:0;top:130px;width:690px;height:528px;background:linear-gradient(90deg,#f4efe9 0%,#e8ddd2 35%,#d6dce6 75%,rgba(214,220,230,0) 100%)}
.hero-title{left:644px;top:300px;font-family:"Montserrat",Arial,sans-serif;font-size:37px;line-height:48px;color:#1d2433;font-weight:400}
.hero-title b{color:var(--red);font-weight:700}
.hero-text{left:644px;top:418px;width:420px;font-size:15px;line-height:26px;color:#333}
.arrow{width:48px;height:48px;border-radius:50%;background:rgba(120,120,120,.55)}

/* services */
.services-title{left:0;top:730px;width:1200px;font-size:33px}
.intro{left:200px;width:800px;text-align:center;font-size:14px;line-height:24px;color:var(--muted)}
.service{width:230px;text-align:center}
.service-icon{width:96px;height:96px;margin:0 auto;border-radius:50%;border:3px solid #1c2f7a;background:#fff;display:flex;align-items:center;justify-content:center}
.service-name{margin-top:20px;font-family:"Montserrat",Arial,sans-serif;font-weight:600;font-size:19px;color:#111}
.service-text{margin:14px auto 0;width:180px;font-size:13px;line-height:19px;color:var(--muted)}
.more{display:inline-block;margin-top:12px;width:38px;height:14px;background:var(--red);color:#fff;font-size:8px;line-height:14px;font-weight:700}

/* portfolio */
.portfolio{left:0;top:1205px;width:1200px;height:568px;background:var(--grey)}
.portfolio-title{left:0;top:1276px;width:1200px;font-size:33px}
.shot{top:1410px;width:229px;height:281px}
.nav-chevron{font-size:40px;color:#aaa;font-family:Arial,sans-serif}

/* testimonials */
.testimonials{left:0;top:1773px;width:1200px;height:383px;background:#fff;box-shadow:0 14px 24px rgba(0,0,0,.06)}
.testimonials-title{left:0;top:1848px;width:1200px;font-size:33px}
.quote-text{left:200px;top:1918px;width:800px;text-align:center;font-size:14px;line-height:25px;color:var(--muted)}
.quote-mark{font-family:Georgia,serif;font-size:90px;color:#ddd;line-height:1}
.client-name{left:0;top:2020px;width:1200px;text-align:center;font-weight:700;font-size:15px;color:#222}
.dots{left:575px;top:2060px;display:flex;gap:8px}
.dots i{width:10px;height:10px;border-radius:50%;background:#222}
.dots i.active{background:var(--red)}

/* clients */
.client{top:2213px;width:157px;height:91px;border:1px solid var(--line);display:flex;align-items:center;justify-content:center;font-family:"Montserrat",Arial,sans-serif;font-weight:700;font-size:16px;color:#222;background:#fff}

/* footer */
.site-footer{left:0;top:2360px;width:1200px;height:435px;background:linear-gradient(180deg,#0f2142 0%,#0c1a34 60%,#0a1528 100%)}
.footer-title{left:140px;top:2436px;font-family:"Montserrat",Arial,sans-serif;font-weight:700;font-size:33px;color:#fff;letter-spacing:1px}
.contact-line{left:140px;display:flex;align-items:center;gap:14px;font-size:14px;color:#c9d2e3}
.social{top:2670px;width:38px;height:38px;border-radius:50%;border:2px solid #9aa7c0}
.field{border:1px solid #3a4d74;background:rgba(10,20,40,.5);color:#aab4c8;font-size:13px;padding:13px 12px}
.send{left:488px;top:2644px;width:570px;height:46px;background:#1d5fae;color:#fff;font-weight:700;font-size:15px;letter-spacing:1px;text-align:center;line-height:46px}
.copyright{left:0;top:2795px;width:1200px;height:42px;line-height:42px;text-align:center;font-size:13px;color:#333;background:#fff}
</style>
</head>
<body>

<div class="abs top-bar"></div>
<div class="abs top-link account">&#9679; MY Vantrel</div>
<div class="abs top-link register">&#9632; Register</div>

<header class="abs site-header"></header>
<div class="abs brand"><span class="brand-dot"></span><span class="brand-name">Vantrel</span></div>
<nav class="abs main-nav"><span>ABOUT US</span><span>SERVICES</span><span>CLIENTS</span><span>CONTACT US</span></nav>

<section class="abs hero"></section>
<div class="abs hero-photo" role="img" aria-label="Photo of a smiling support agent wearing a headset with colleagues at work behind her"></div>
<h1 class="abs hero-title">We Provide High Quality<br>Professional <b>IT SERVICES</b></h1>
<p class="abs hero-text">Lorem Ipsum is simply dummy text of the printing and typesetting industry Lorem Ipsum has been.</p>
<div class="abs arrow" style="left:28px;top:393px"><svg width="48" height="48"><path d="M28 14 L18 24 L28 34" stroke="#fff" stroke-width="3" fill="none"/></svg></div>
<div class="abs arrow" style="left:1120px;top:393px"><svg width="48" height="48"><path d="M20 14 L30 24 L20 34" stroke="#fff" stroke-width="3" fill="none"/></svg></div>

<h2 class="abs heading services-title">SERVICES WE PROVIDE</h2>
<p class="abs intro" style="top:786px">Lorem Ipsum is simply dummy text of the printing and typesetting industry. Lorem Ipsum has been the industry's standard dummy text ever since the 1500s, when an unknown printer took a galley of type and scrambled</p>

<div class="abs service" style="left:112px;top:882px">
  <div class="service-icon"><svg width="56" height="56"><circle cx="28" cy="28" r="22" fill="#e8eef8"/><path d="M16 40 L36 18 L40 22 L20 44 Z" fill="#b01a1a"/></svg></div>
  <div class="service-name">Websites Design</div>
  <p class="service-text">Lorem Ipsum. Proin gravida nibh vel velit auctor aliquet. Aenean sollicitudin.</p>
  <span class="more">more</span>
</div>
<div class="abs service" style="left:359px;top:882px">
  <div class="service-icon"><svg width="56" height="56"><circle cx="28" cy="28" r="22" fill="#1e5fb8"/><ellipse cx="28" cy="28" rx="10" ry="22" fill="none" stroke="#9cc2ee" stroke-width="2"/><line x1="6" y1="28" x2="50" y2="28" stroke="#9cc2ee" stroke-width="2"/></svg></div>
  <div class="service-name">Hosting</div>
  <p class="service-text">Lorem Ipsum. Proin gravida nibh vel velit auctor aliquet. Aenean sollicitudin.</p>
  <span class="more">more</span>
</div>
<div class="abs service" style="left:606px;top:882px">
  <div class="service-icon"><svg width="56" height="56"><path d="M28 28 L28 6 A22 22 0 0 1 50 28 Z" fill="#e8a21a"/><path d="M28 28 L50 28 A22 22 0 0 1 12 43 Z" fill="#1e5fb8"/><path d="M28 28 L12 43 A22 22 0 0 1 28 6 Z" fill="#3aa655"/></svg></div>
  <div class="service-name">Online Marketing</div>
  <p class="service-text">Lorem Ipsum. Proin gravida nibh vel velit auctor aliquet. Aenean sollicitudin.</p>
  <span class="more">more</span>
</div>
<div class="abs service" style="left:853px;top:882px">
  <div class="service-icon"><svg width="56" height="56"><circle cx="28" cy="28" r="21" fill="#d9302b"/><circle cx="28" cy="28" r="9" fill="#fff"/><rect x="24" y="7" width="8" height="42" fill="#fff" opacity=".85"/><rect x="7" y="24" width="42" height="8" fill="#fff" opacity=".85"/></svg></div>
  <div class="service-name">Support</div>
  <p class="service-text">Lorem Ipsum. Proin gravida nibh vel velit auctor aliquet. Aenean sollicitudin.</p>
  <span class="more">more</span>
</div>

<section class="abs portfolio"></section>
<h2 class="abs heading portfolio-title">OUR PORTFOLIO</h2>
<p class="abs intro" style="top:1330px">Lorem Ipsum is simply dummy text of the printing and typesetting industry. Lorem Ipsum has been the industry's</p>
<div class="abs shot" style="left:142px;background:linear-gradient(180deg,#f4f4f4,#dfe4ec)" role="img" aria-label="Portfolio preview of a corporate website"></div>
<div class="abs shot" style="left:371px;background:linear-gradient(180deg,#1a1a1a,#8a1010 60%,#222)" role="img" aria-label="Portfolio preview of a dark red business website"></div>
<div class="abs shot" style="left:600px;background:linear-gradient(180deg,#3d9fd6,#e8eef2 55%,#f5f5f5)" role="img" aria-label="Portfolio preview of a blue web services website"></div>
<div class="abs shot" style="left:829px;background:linear-gradient(180deg,#e35a5a 0 14%,#eef3f8 14% 85%,#3b4a66 85%)" role="img" aria-label="Portfolio preview of an advertising website"></div>
<div class="abs nav-chevron" style="left:86px;top:1525px">&#8249;</div>
<div class="abs nav-chevron" style="left:1093px;top:1525px">&#8250;</div>

<section class="abs testimonials"></section>
<h2 class="abs heading testimonials-title">TESTIMONIALS</h2>
<div class="abs quote-mark" style="left:168px;top:1898px">&ldquo;</div>
<p class="abs quote-text">Lorem ipsum dolor sit amet, consectetur adipiscing elit. Suspendisse a nunc ultrices dolor rutrum lacinia at non eros. Suspendisse vel pulvinar augue, eu viverra mauris. Nulla facilisi. Class aptent taciti sociosqu ad litora torquent per conubia nostra, per inceptos himenaeos. In a enim tincidunt.</p>
<div class="abs quote-mark" style="left:808px;top:1950px">&rdquo;</div>
<div class="abs client-name">- CLIENT NAME</div>
<div class="abs dots"><i class="active"></i><i></i><i></i><i></i></div>

<div class="abs client" style="left:142px">Summit Arcade</div>
<div class="abs client" style="left:331px">Northwire</div>
<div class="abs client" style="left:520px">Pixelbay</div>
<div class="abs client" style="left:709px">Daily Ledger</div>
<div class="abs client" style="left:898px">Kestrel Goods</div>

<footer class="abs site-footer"></footer>
<h2 class="abs footer-title">CONTACT US</h2>
<div class="abs contact-line" style="top:2502px"><svg width="12" height="16"><path d="M6 0 A6 6 0 0 1 12 6 C12 10 6 16 6 16 C6 16 0 10 0 6 A6 6 0 0 1 6 0Z" fill="#c9d2e3"/><circle cx="6" cy="6" r="2" fill="#0e1a33"/></svg>1234 Street Name, City Name, United States</div>
<div class="abs contact-line" style="top:2532px"><svg width="12" height="16"><path d="M2 1 L5 1 L6 5 L4 6 C5 9 7 11 10 12 L11 10 L12 11 L12 15 C6 15 1 10 1 2Z" fill="#c9d2e3"/></svg>(1234) 567-907</div>
<div class="abs contact-line" style="top:2561px"><svg width="14" height="12"><rect x="0" y="1" width="14" height="10" fill="#c9d2e3"/><path d="M0 1 L7 7 L14 1" stroke="#0e1a33" fill="none"/></svg>contact@vantrel.example</div>
<div class="abs social" style="left:138px"></div>
<div class="abs social" style="left:180px"></div>
<div class="abs social" style="left:222px"></div>
<div class="abs social" style="left:264px"></div>

<div class="abs field" style="left:488px;top:2446px;width:275px;height:48px">Your name...</div>
<div class="abs field" style="left:783px;top:2446px;width:275px;height:48px">Your email address...</div>
<div class="abs field" style="left:488px;top:2514px;width:570px;height:116px">Message...</div>
<div class="abs send">SEND MESSAGE</div>

<div class="abs copyright">&copy; Copyright 2014 - Vantrel. All rights reserved.</div>

</body>
</html>
```